Personal Development Model Graphic

I am creating a Personal Development/Coaching business and website and need some assistance with the development of a graphic that represents my methodology. I have already done what I consider to be a working version, but now it's time to have a professional design eye take a look at it and improve.

Specifically, I need assistance on color usage. I'd like each of the 8 areas of the model to have a color, and I've tried to utilize colors I feel are representative of the specific area(for example, purple for spirituality) but it doesn't really work for everything and perhaps additional thought could be put to that aspect of it.

Also, the model needs to work in reverse of the way it's pictured in the attached JPEG. So Friends needs to be first (top center)and then going clockwise, Spirituality needs to be in the 1:00 position not the 11:00 position and then continue around to Community, Family, Exercise, Career, Art/Creativity, and last at 11:00 Sexuality. I was going to update it before uploading, but I'm having trouble with Photoshop and just decided to pull the trigger on having a designer do it.

Thank you in advance for your creativity and ideas!

Industry/Entity Type

Business

Requirements
Nice to have
• It would be fantastic if it could feel modern, and high tech. I realize this is difficult with circles! But whatever you can do.

On color usage, it would again be wonderful to have colors that are more modern than traditional. I'll leave that to your discretion.

```html
<!DOCTYPE html>
<html lang="en">
<head>
<meta charset="utf-8">
<title>Happiness – Personal Development Model</title>
<link rel="stylesheet" href="https://fonts.googleapis.com/css2?family=Russo+One&display=swap">
<style>
  :root {
    --bg: #ffffff;
    --disc: #ececec;
    --label: #222222;
    --title: #14134f;
    --core: #1a6fb5;
    --core-light: #c9e0ef;
    --friends: #e6501c;
    --spirituality: #5a2686;
    --community: #3a2312;
    --family: #17663a;
    --exercise: #ecd51c;
    --career: #28287c;
    --art: #e0166f;
    --sexuality: #b01e2a;
  }
  html, body {
    margin: 0;
    padding: 0;
    width: 1200px;
    height: 1000px;
    overflow: hidden;
    background: var(--bg);
  }
  .model { display: block; width: 1200px; height: 1000px; }
  .model__label {
    font-family: "Russo One", sans-serif;
    font-size: 22px;
    letter-spacing: 1px;
    fill: var(--label);
    text-anchor: middle;
  }
  .model__title {
    font-family: "Russo One", sans-serif;
    font-size: 52px;
    letter-spacing: 2px;
    fill: var(--title);
    text-anchor: middle;
  }
  .disc { fill: var(--disc); }
  .ring { fill: none; stroke-width: 15; }
  .core-ring { fill: none; stroke-width: 26; }

  .tone-core stop { stop-color: var(--core); }
  .tone-core stop.light { stop-color: var(--core-light); }
  .tone-friends stop { stop-color: var(--friends); }
  .tone-spirituality stop { stop-color: var(--spirituality); }
  .tone-community stop { stop-color: var(--community); }
  .tone-family stop { stop-color: var(--family); }
  .tone-exercise stop { stop-color: var(--exercise); }
  .tone-career stop { stop-color: var(--career); }
  .tone-art stop { stop-color: var(--art); }
  .tone-sexuality stop { stop-color: var(--sexuality); }
  stop.fade { stop-opacity: 0.25; }
  stop.soft { stop-opacity: 0.55; }
</style>
</head>
<body>
<svg class="model" viewBox="0 0 1200 1000" xmlns="http://www.w3.org/2000/svg" role="img" aria-label="Happiness model with eight life areas">
  <defs>
    <!-- ring strokes: pale top-left to full colour bottom-right -->
    <linearGradient id="ring-friends" class="tone-friends" x1="0" y1="0" x2="1" y2="1"><stop offset="0" class="fade"/><stop offset="0.55"/></linearGradient>
    <linearGradient id="ring-spirituality" class="tone-spirituality" x1="0" y1="0" x2="1" y2="1"><stop offset="0" class="fade"/><stop offset="0.55"/></linearGradient>
    <linearGradient id="ring-community" class="tone-community" x1="0" y1="0" x2="1" y2="1"><stop offset="0" class="fade"/><stop offset="0.55"/></linearGradient>
    <linearGradient id="ring-family" class="tone-family" x1="0" y1="0" x2="1" y2="1"><stop offset="0" class="fade"/><stop offset="0.55"/></linearGradient>
    <linearGradient id="ring-exercise" class="tone-exercise" x1="0" y1="0" x2="1" y2="1"><stop offset="0" class="fade"/><stop offset="0.55"/></linearGradient>
    <linearGradient id="ring-career" class="tone-career" x1="0" y1="0" x2="1" y2="1"><stop offset="0" class="fade"/><stop offset="0.55"/></linearGradient>
    <linearGradient id="ring-art" class="tone-art" x1="0" y1="0" x2="1" y2="1"><stop offset="0" class="fade"/><stop offset="0.55"/></linearGradient>
    <linearGradient id="ring-sexuality" class="tone-sexuality" x1="0" y1="0" x2="1" y2="1"><stop offset="0" class="fade"/><stop offset="0.55"/></linearGradient>
    <linearGradient id="ring-core" class="tone-core" x1="0" y1="0" x2="1" y2="1"><stop offset="0" class="light"/><stop offset="0.5"/></linearGradient>

    <!-- connector fills: soft near the area circle, full near the core -->
    <linearGradient id="link-friends" class="tone-friends" gradientUnits="userSpaceOnUse" x1="0" y1="200" x2="0" y2="310"><stop offset="0" class="soft"/><stop offset="1"/></linearGradient>
    <linearGradient id="link-spirituality" class="tone-spirituality" gradientUnits="userSpaceOnUse" x1="0" y1="200" x2="0" y2="310"><stop offset="0" class="soft"/><stop offset="1"/></linearGradient>
    <linearGradient id="link-community" class="tone-community" gradientUnits="userSpaceOnUse" x1="0" y1="200" x2="0" y2="310"><stop offset="0" class="soft"/><stop offset="1"/></linearGradient>
    <linearGradient id="link-family" class="tone-family" gradientUnits="userSpaceOnUse" x1="0" y1="200" x2="0" y2="310"><stop offset="0" class="soft"/><stop offset="1"/></linearGradient>
    <linearGradient id="link-exercise" class="tone-exercise" gradientUnits="userSpaceOnUse" x1="0" y1="200" x2="0" y2="310"><stop offset="0" class="soft"/><stop offset="1"/></linearGradient>
    <linearGradient id="link-career" class="tone-career" gradientUnits="userSpaceOnUse" x1="0" y1="200" x2="0" y2="310"><stop offset="0" class="soft"/><stop offset="1"/></linearGradient>
    <linearGradient id="link-art" class="tone-art" gradientUnits="userSpaceOnUse" x1="0" y1="200" x2="0" y2="310"><stop offset="0" class="soft"/><stop offset="1"/></linearGradient>
    <linearGradient id="link-sexuality" class="tone-sexuality" gradientUnits="userSpaceOnUse" x1="0" y1="200" x2="0" y2="310"><stop offset="0" class="soft"/><stop offset="1"/></linearGradient>

    <polygon id="link-shape" points="542,195 658,195 624,312 576,312"/>
  </defs>

  <!-- connectors -->
  <g class="links">
    <use href="#link-shape" fill="url(#link-friends)" transform="rotate(0 600 497)"/>
    <use href="#link-spirituality-shape" />
    <use href="#link-shape" fill="url(#link-spirituality)" transform="rotate(45 600 497)"/>
    <use href="#link-shape" fill="url(#link-community)" transform="rotate(90 600 497)"/>
    <use href="#link-shape" fill="url(#link-family)" transform="rotate(135 600 497)"/>
    <use href="#link-shape" fill="url(#link-exercise)" transform="rotate(180 600 497)"/>
    <use href="#link-shape" fill="url(#link-career)" transform="rotate(225 600 497)"/>
    <use href="#link-shape" fill="url(#link-art)" transform="rotate(270 600 497)"/>
    <use href="#link-shape" fill="url(#link-sexuality)" transform="rotate(315 600 497)"/>
  </g>

  <!-- core -->
  <g class="core">
    <circle class="disc" cx="600" cy="497" r="178"/>
    <circle class="core-ring" cx="600" cy="497" r="184" stroke="url(#ring-core)"/>
    <text class="model__title" x="600" y="515">HAPPINESS</text>
  </g>

  <!-- life areas -->
  <g class="area area--friends">
    <circle class="disc" cx="600" cy="125" r="100"/>
    <circle class="ring" cx="600" cy="125" r="100" stroke="url(#ring-friends)"/>
    <text class="model__label" x="600" y="133">FRIENDS</text>
  </g>
  <g class="area area--spirituality">
    <circle class="disc" cx="863" cy="235" r="100"/>
    <circle class="ring" cx="863" cy="235" r="100" stroke="url(#ring-spirituality)"/>
    <text class="model__label" x="863" y="243">SPIRITUALITY</text>
  </g>
  <g class="area area--community">
    <circle class="disc" cx="973" cy="497" r="100"/>
    <circle class="ring" cx="973" cy="497" r="100" stroke="url(#ring-community)"/>
    <text class="model__label" x="973" y="505">COMMUNITY</text>
  </g>
  <g class="area area--family">
    <circle class="disc" cx="863" cy="760" r="100"/>
    <circle class="ring" cx="863" cy="760" r="100" stroke="url(#ring-family)"/>
    <text class="model__label" x="863" y="768">FAMILY</text>
  </g>
  <g class="area area--exercise">
    <circle class="disc" cx="600" cy="870" r="100"/>
    <circle class="ring" cx="600" cy="870" r="100" stroke="url(#ring-exercise)"/>
    <text class="model__label" x="600" y="878">EXERCISE</text>
  </g>
  <g class="area area--career">
    <circle class="disc" cx="337" cy="760" r="100"/>
    <circle class="ring" cx="337" cy="760" r="100" stroke="url(#ring-career)"/>
    <text class="model__label" x="337" y="768">CAREER</text>
  </g>
  <g class="area area--art">
    <circle class="disc" cx="227" cy="497" r="100"/>
    <circle class="ring" cx="227" cy="497" r="100" stroke="url(#ring-art)"/>
    <text class="model__label" x="227" y="490">ART</text>
    <text class="model__label" x="227" y="521">CREATIVITY</text>
  </g>
  <g class="area area--sexuality">
    <circle class="disc" cx="337" cy="235" r="100"/>
    <circle class="ring" cx="337" cy="235" r="100" stroke="url(#ring-sexuality)"/>
    <text class="model__label" x="337" y="243">SEXUALITY</text>
  </g>
</svg>
</body>
</html>
```